Business Card Design Project

A business card for a new company in Ontario Canada called Sketch for Growth. It is a consulting company which uses Brixel as the medium for facilitation.

The target market is for senior leaders in healthcare and social services.

Industry/Entity Type

Healthcare

Requirements
Must have
• The name Sketch For Growth
Dana Moreheuse RRT, B Ed (AD ed).
Tacticraft Facililitator (R)

Tag Line
Engaging Transforming and Innovative
The attached logo

danamoreheuse@mailnook.com
555-284-9137
Should not have
• Lime green
Times New Roman or Arial font
Do not include Brixel bricks on the card.

```html
<!DOCTYPE html>
<html lang="en">
<head>
<meta charset="utf-8">
<title>Sketch For Growth – Business Card</title>
<link rel="stylesheet" href="https://fonts.googleapis.com/css2?family=Caudex&family=Marcellus+SC&family=Fira+Sans:ital,wght@0,500;0,600;1,400&display=swap">
<style>
  :root {
    --purple: #4b0a80;
    --sky: #3d9bd1;
    --edge-line: #6fb3de;
    --ink-grey: #8a8a8a;
    --ink: #1c1c1c;
    --card: #ffffff;
    --backdrop: #ececec;
  }
  * { margin: 0; padding: 0; box-sizing: border-box; }
  html, body { width: 1200px; height: 900px; overflow: hidden; }
  body { background: var(--backdrop); position: relative; }

  .business-card {
    position: absolute;
    left: 180px; top: 195px;
    width: 840px; height: 510px;
    background: var(--card);
    overflow: hidden;
    box-shadow: 0 2px 10px rgba(0,0,0,0.12);
  }
  .side-waves { position: absolute; inset: 0; width: 840px; height: 510px; }

  .brand {
    position: absolute; left: 0; right: 0; top: 150px;
    display: flex; justify-content: center; align-items: center; gap: 14px;
  }
  .brand-mark { width: 18px; height: 18px; background: var(--purple); border-radius: 50%; }
  .brand-name {
    font-family: "Marcellus SC", serif;
    font-size: 40px; color: var(--purple); letter-spacing: 1px;
  }
  .tagline {
    position: absolute; left: 0; right: 0; top: 240px; text-align: center;
    font-family: "Caudex", serif; font-size: 20px; color: var(--ink-grey);
  }
  .person {
    position: absolute; left: 0; right: 0; top: 328px; text-align: center;
  }
  .person-name {
    font-family: "Marcellus SC", serif; font-size: 32px; color: var(--purple);
  }
  .credentials {
    font-family: "Fira Sans", sans-serif; font-style: italic;
    font-size: 15px; color: var(--ink); margin-left: 4px;
  }
  .role {
    position: absolute; left: 0; right: 0; top: 380px; text-align: center;
    font-family: "Fira Sans", sans-serif; font-weight: 500;
    font-size: 24px; color: var(--sky);
  }
  .contact {
    position: absolute; top: 450px;
    display: flex; align-items: center; gap: 18px;
    font-family: "Fira Sans", sans-serif; font-weight: 500;
    font-size: 19px; color: var(--sky);
  }
  .contact-phone { left: 116px; }
  .contact-email { left: 360px; }
  .contact-bullet { width: 24px; height: 24px; background: var(--purple); }
</style>
</head>
<body>
  <div class="business-card">
    <svg class="side-waves" viewBox="0 0 840 510" aria-hidden="true">
      <path d="M0 0 H36 C20 60 80 120 70 200 C62 270 20 300 36 380 C44 440 70 470 60 510 H0 Z" fill="var(--purple)"/>
      <path d="M36 0 C20 60 80 120 70 200 C62 270 20 300 36 380 C44 440 70 470 60 510" fill="none" stroke="var(--edge-line)" stroke-width="2"/>
      <path d="M840 0 H800 C820 60 810 120 820 200 C830 280 800 330 790 400 C785 460 810 490 800 510 H840 Z" fill="var(--purple)"/>
      <path d="M800 0 C820 60 810 120 820 200 C830 280 800 330 790 400 C785 460 810 490 800 510" fill="none" stroke="var(--edge-line)" stroke-width="2"/>
    </svg>

    <div class="brand">
      <span class="brand-mark"></span>
      <span class="brand-name">Sketch For Growth</span>
    </div>
    <p class="tagline">Engaging Transforming and Innovative</p>

    <p class="person"><span class="person-name">Dana Moreheuse</span><span class="credentials">RRT, BA (AD ed)</span></p>
    <p class="role">Tacticraft Facilitator (R)</p>

    <p class="contact contact-phone"><span class="contact-bullet"></span>555-284-9137</p>
    <p class="contact contact-email"><span class="contact-bullet"></span>danamoreheuse@mailnook.com</p>
  </div>
</body>
</html>
```